Property developer, money partner needs business card design using logo concept provided

Our company develops residential properties, does money lends for joint ventures in property deals and finds property deals for other money partners. We have provided a basic logo for you to work from. Any graphic or logo design on the card is to communicate development and finance collaboration. Color choice is not so important for us, but color choice does need to reflect professionalism.

```html
<!DOCTYPE html>
<html lang="en">
<head>
<meta charset="utf-8">
<title>Brightfield Property Partners – Business Card</title>
<link href="https://fonts.googleapis.com/css2?family=Montserrat:wght@400;500;700&display=swap" rel="stylesheet">
<style>
  :root {
    --bg-light: #ececec;
    --bg-dark: #8a8a8a;
    --blue-light: #6a88b6;
    --blue-mid: #3f619a;
    --blue-deep: #1c4586;
    --card-white: #ebebeb;
    --text-white: #ffffff;
    --accent-red: #c0282d;
  }
  * { box-sizing: border-box; margin: 0; padding: 0; }
  html, body { width: 1200px; height: 1200px; overflow: hidden; }
  body {
    background: linear-gradient(110deg, var(--bg-light) 0%, #c9c9c9 55%, var(--bg-dark) 100%);
    font-family: "Montserrat", Arial, sans-serif;
    position: relative;
  }
  .card {
    position: absolute;
    left: 220px;
    width: 760px;
    height: 434px;
    border-radius: 26px;
    overflow: hidden;
    background: linear-gradient(100deg, var(--blue-light) 0%, var(--blue-mid) 40%, var(--blue-deep) 75%);
    box-shadow: 0 6px 0 #163a75, 0 18px 30px rgba(0,0,0,0.25);
    color: var(--text-white);
  }
  .card-front { top: 110px; }
  .card-back { top: 650px; }

  /* front */
  .brand {
    position: absolute;
    left: 0; right: 0; top: 170px;
    display: flex; align-items: center; justify-content: center; gap: 14px;
  }
  .brand-dot {
    width: 34px; height: 34px; border-radius: 50%;
    background: var(--text-white);
  }
  .brand-name {
    font-weight: 700; font-size: 30px; letter-spacing: 2px;
    color: var(--text-white);
  }
  .brand-reg {
    position: absolute; left: 0; right: 0; top: 230px;
    text-align: center; font-size: 12px; letter-spacing: 3px; font-weight: 400;
  }

  /* back */
  .panel {
    position: absolute; top: 0; right: 0; width: 330px; height: 100%;
  }
  .panel-name {
    position: absolute; right: 40px; top: 196px; width: 250px;
    display: flex; align-items: center; gap: 12px;
    color: var(--blue-deep); font-weight: 700; font-size: 24px; letter-spacing: 1px;
  }
  .panel-dot { width: 28px; height: 28px; border-radius: 50%; background: var(--blue-deep); flex: none; }
  .person { position: absolute; left: 48px; top: 48px; }
  .person-name { font-weight: 700; font-size: 34px; }
  .person-role { font-weight: 500; font-size: 19px; margin-top: 6px; }
  .address { position: absolute; left: 86px; top: 252px; font-size: 18px; line-height: 1.4; font-weight: 500; }
  .contacts { position: absolute; left: 86px; top: 308px; list-style: none; font-size: 18px; font-weight: 500; }
  .contacts li { display: flex; align-items: center; gap: 12px; line-height: 1.55; }
  .contacts svg { width: 16px; height: 16px; flex: none; }
</style>
</head>
<body>
  <section class="card card-front" aria-label="Card front">
    <div class="brand">
      <span class="brand-dot"></span>
      <span class="brand-name">BRIGHTFIELD</span>
    </div>
    <p class="brand-reg">PROPERTY PARTNERS · A.C.N 418 903 256</p>
  </section>

  <section class="card card-back" aria-label="Card back">
    <svg class="panel" viewBox="0 0 330 434" preserveAspectRatio="none" aria-hidden="true">
      <polygon points="120,0 330,0 330,434 0,434 0,410" fill="var(--card-white)"/>
    </svg>
    <div class="panel-name"><span class="panel-dot"></span>BRIGHTFIELD</div>

    <div class="person">
      <h1 class="person-name">Marcus Delaney</h1>
      <p class="person-role">Founder &amp; Director</p>
    </div>

    <p class="address">418 Harbor Lane<br>Fairview Oregon 97024</p>

    <ul class="contacts">
      <li>
        <svg viewBox="0 0 24 24" aria-hidden="true"><path fill="#fff" d="M6.6 10.8a15 15 0 0 0 6.6 6.6l2.2-2.2c.3-.3.7-.4 1-.2 1.1.4 2.3.6 3.6.6.6 0 1 .4 1 1V20c0 .6-.4 1-1 1A17 17 0 0 1 3 4c0-.6.4-1 1-1h3.5c.6 0 1 .4 1 1 0 1.3.2 2.5.6 3.6.1.3 0 .7-.2 1z"/></svg>
        (555)-310-4782
      </li>
      <li>
        <svg viewBox="0 0 24 24" aria-hidden="true"><rect x="2" y="5" width="20" height="14" rx="1" fill="#fff"/><path d="M3 6l9 7 9-7" fill="none" stroke="#2d5290" stroke-width="2"/></svg>
        info@brightfieldpartners.co
      </li>
      <li>
        <svg viewBox="0 0 24 24" aria-hidden="true"><circle cx="12" cy="12" r="10" fill="#fff"/><path d="M2 12h20M12 2c3 3 3 17 0 20M12 2c-3 3-3 17 0 20" fill="none" stroke="#2d5290" stroke-width="1.6"/></svg>
        www.brightfieldpartners.co
      </li>
    </ul>
  </section>
</body>
</html>
```